Lumetta small bites needs a website.

I have a small dessert bite catering business creating uniquely crafted small dessert bites made with high quality ingredients focusing on gluten free and vegan options.
I would like a website to show off my creations and provide a way for customers to reach me. I work out of a catering kitchen so would include the address of the kitchen as well as my phone number and email etc.

I already own the “www.lumettasmallbites.example” domain but have not used it yet. I have zero knowledge on website creation and design so need help in design as well as coding. I’m not sure how many pages I need designed. I would like one for the dessert bar / catering focus and one for my tasting boxes. I would like a way to upload new tasting box pictures and information to the website as they come out.

Target Market(s)

Individuals or businesses wanting to buy small bite desserts for weddings, gatherings and events for a dessert bar table. I also am creating monthly / seasonal tasting boxes (holiday, Valentine’s Day, etc) that I’d like to highlight.

Industry/Entity Type

Dessert catering, vegan and gluten free

Coding

Coded - Design and coding required

Number of Pages Required

2 page

Colors
E54698
E96AAD
F1A4CE
F9D9EA
FCEFF6

Requirements
Must have
• Pictures of my desserts and text explaining my process of creating individual flavor profiled desserts for people. I would like it to match the current color scheme and vibe of my logo. Must say that I am a catering company so don’t have a bakery but do have frozen tasting boxes available at the store front of the commercial kitchen that I use.
Nice to have
• I would like the website to have the vibe and colors of my logo but would welcome additional creativity from the designer. Include pink and brown as the main colors

```html
<!DOCTYPE html>
<html lang="en">
<head>
<meta charset="utf-8">
<title>Lumetta Small Bite Catering</title>
<link href="https://fonts.googleapis.com/css2?family=Great+Vibes&family=Lato:wght@400;700&display=swap" rel="stylesheet">
<style>
:root{
  --pink:#e54698;
  --pink-mid:#e96aad;
  --pink-soft:#f1a4ce;
  --pink-pale:#f9d9ea;
  --blush:#fceff6;
  --bg:#1b1a1a;
  --bg-deep:#141313;
  --card:#221f1f;
  --line:#6e5a63;
  --text:#f2eef0;
  --muted:#cfc7cb;
}
*{box-sizing:border-box;margin:0;padding:0}
html,body{width:1200px;height:4652px;overflow:hidden}
body{background:var(--bg);color:var(--text);font-family:"Lato",Arial,sans-serif;position:relative}
.abs{position:absolute}
.photo{position:absolute;border-radius:14px}
.script{font-family:"Great Vibes",cursive;color:var(--text);font-size:36px;line-height:40px;text-align:center;word-spacing:.25em}
.heading{font-family:"Lato",Arial,sans-serif;color:var(--pink);font-size:44px;line-height:50px;font-weight:400;letter-spacing:1px;text-transform:uppercase;text-align:center}
.btn{display:inline-block;border-radius:30px;font-size:16px;padding:12px 24px;text-decoration:none;white-space:nowrap}
.btn-pink{background:var(--pink);color:#fff}
.btn-outline{border:1.5px solid var(--text);color:var(--text)}
/* navigation */
.nav{left:160px;top:40px;width:880px;height:48px;background:var(--pink);border-radius:24px;font-size:14px;text-transform:uppercase;letter-spacing:.5px}
.nav a{color:#fff;text-decoration:none;position:absolute;top:16px}
.logo-badge{border-radius:50%;background:#fff;border:4px solid var(--pink);display:flex;align-items:center;justify-content:center;color:var(--pink);font-weight:700}
/* hero */
.hero-title{left:112px;top:196px;font-size:42px;line-height:1.18;letter-spacing:2px;text-transform:uppercase;font-weight:400}
.hero-text{left:112px;top:364px;width:440px;font-size:17px;line-height:1.5}
/* process */
.steps{left:112px;top:1360px;width:976px;display:flex;gap:18px}
.step{flex:1;height:300px;border:1.5px solid var(--line);border-radius:22px;background:var(--card);padding:22px 16px;text-align:center}
.step-icon{width:60px;height:60px;border-radius:50%;background:var(--pink);margin:0 auto 18px;display:flex;align-items:center;justify-content:center}
.step h3{color:var(--pink);font-size:16px;font-weight:700;margin-bottom:18px;text-transform:uppercase}
.step p{font-size:13px;line-height:1.5;color:var(--muted)}
/* gallery */
.gallery{left:112px;top:1948px;width:976px;display:grid;grid-template-columns:repeat(3,1fr);grid-template-rows:296px 296px;gap:20px 16px}
.gallery .tile{border-radius:14px}
/* seasonal */
.seasonal{left:0;top:2768px;width:1200px;height:392px}
.seasonal-panel{left:212px;top:2864px;width:776px;height:256px;background:rgba(20,18,18,.9);border-radius:20px;text-align:center;padding-top:22px}
/* audience */
.aud-card{top:3620px;height:420px;border-radius:20px}
.aud-label{top:4070px;text-align:center;font-size:15px}
.aud-label b{display:block;color:var(--pink);font-weight:700;text-transform:uppercase;margin-bottom:6px}
/* footer */
.footer{left:0;top:4208px;width:1200px;height:420px;background:var(--bg-deep);border-top:1px solid #333}
.contact{left:380px;top:4368px;width:440px;text-align:center;font-size:15px;line-height:1.75}
.social{top:4492px;width:32px;height:32px;border-radius:50%;background:var(--pink)}
.legal{left:0;top:4624px;width:1200px;height:28px;background:#0b0a0a;text-align:center;font-size:12px;line-height:28px;color:var(--muted)}
</style>
</head>
<body>

<nav class="abs nav">
  <a style="left:84px">Home</a>
  <a style="left:168px">Dessert Bar Catering</a>
  <a style="left:540px">Tasting Boxes</a>
  <a style="left:676px">About</a>
  <a style="left:760px">Contact</a>
</nav>
<div class="abs logo-badge" style="left:542px;top:8px;width:116px;height:116px;font-size:22px">Lumetta</div>

<h1 class="abs hero-title">Thoughtfully<br>crafted dessert<br>experiences</h1>
<p class="abs hero-text">From dessert bars for celebrations to seasonal tasting boxes, Lumetta creates small bites that are rich in flavor, balance, and care.</p>
<a class="abs btn btn-pink" style="left:112px;top:470px">Plan Your Dessert Bar</a>
<a class="abs btn btn-outline" style="left:340px;top:470px">Seasonal Tasting Boxes</a>
<p class="abs hero-text" style="top:542px;font-size:16px">Dessert catering company operating out of a licensed commercial kitchen.</p>

<div class="photo" role="img" aria-label="Iced mini cakes on a tray" style="left:812px;top:132px;width:128px;height:180px;background:radial-gradient(circle at 40% 35%,#efe4d2,#b08a66 55%,#5a3526)"></div>
<div class="photo" role="img" aria-label="Mini cheesecakes with pink trim" style="left:948px;top:132px;width:124px;height:180px;background:radial-gradient(circle at 50% 45%,#f4ead6,#d4b68c 55%,#8a5f42);border:4px solid var(--pink)"></div>
<div class="photo" role="img" aria-label="Chocolate-topped dessert squares" style="left:812px;top:320px;width:128px;height:120px;background:radial-gradient(circle at 45% 40%,#8a5a3e,#4a2a1c 60%,#24140e)"></div>
<div class="photo" role="img" aria-label="Pink frosted cupcake bites" style="left:948px;top:320px;width:124px;height:272px;background:radial-gradient(circle at 50% 35%,#f7c9e0,#e08ab6 45%,#7a4534)"></div>
<div class="photo" role="img" aria-label="Lemon tart bites" style="left:812px;top:448px;width:128px;height:144px;background:radial-gradient(circle at 50% 45%,#f2e6b0,#c6a466 55%,#6e4e30)"></div>

<div class="abs" role="img" aria-label="Assorted dessert bites on a serving board" style="left:-60px;top:716px;width:280px;height:280px;border-radius:50%;background:radial-gradient(circle at 55% 40%,#eee0c8,#b8916a 50%,#5a3526);border:8px solid var(--pink)"></div>
<div class="abs script" style="left:0;top:716px;width:1200px">Our Story</div>
<h2 class="abs heading" style="left:0;top:764px;width:1200px">About us</h2>
<p class="abs" style="left:230px;top:846px;width:740px;font-size:15px;line-height:1.55;text-align:center;color:var(--muted)">At Lumetta Small Bite Catering, every dessert begins with flavor. Each bite is thoughtfully crafted by balancing taste, texture, aroma, and sweetness, creating desserts that feel intentional, refined, and deeply satisfying. Lumetta specializes in small dessert bites designed for dessert bars, gatherings, and celebrations, with a strong focus on vegan and gluten-free options made using high-quality ingredients. Rather than offering a one-size-fits-all menu, each collection is approached as a unique flavor experience, carefully curated to complement the occasion and the people enjoying it.</p>
<a class="abs btn btn-outline" style="left:470px;top:1032px">Learn More About Lumetta</a>
<div class="abs" role="img" aria-label="Chocolate brownie bites" style="left:960px;top:928px;width:280px;height:280px;border-radius:50%;background:radial-gradient(circle at 45% 40%,#8a5a3e,#4a2a1c 55%,#22130d);border:8px solid var(--pink)"></div>

<div class="abs script" style="left:0;top:1212px;width:1200px">The Lumetta Process</div>
<h2 class="abs heading" style="left:0;top:1262px;width:1200px">From flavor to finished bite</h2>
<div class="abs steps">
  <div class="step">
    <div class="step-icon"><svg width="28" height="28" viewBox="0 0 24 24" fill="none" stroke="#fff" stroke-width="2"><circle cx="10" cy="10" r="6"/><path d="M15 15l6 6"/></svg></div>
    <h3>1. Flavor Discovery</h3>
    <p>Every dessert begins with understanding. We start by learning about flavor preferences, dietary needs, and the tone of your event or gathering. This foundation allows each bite to feel personal and purposeful.</p>
  </div>
  <div class="step">
    <div class="step-icon"><svg width="28" height="28" viewBox="0 0 24 24" fill="none" stroke="#fff" stroke-width="2"><path d="M4 20l4-1 11-11-3-3L5 16z"/></svg></div>
    <h3>2. Thoughtful Design</h3>
    <p>Flavors are carefully paired with complementary textures, aromas, and sweetness levels. Each dessert is designed to be balanced and satisfying in just a few bites, never overpowering, always intentional.</p>
  </div>
  <div class="step">
    <div class="step-icon"><svg width="28" height="28" viewBox="0 0 24 24" fill="none" stroke="#fff" stroke-width="2"><path d="M5 3v8M8 3v8M5 11h3M6.5 11v10M17 3c-3 2-3 8 0 9v9"/></svg></div>
    <h3>3. Tasting Refinement</h3>
    <p>Recipes are refined through tasting and adjustment, ensuring that every component works in harmony. This step allows flavors to evolve until they reach their best expression.</p>
  </div>
  <div class="step">
    <div class="step-icon"><svg width="28" height="28" viewBox="0 0 24 24" fill="none" stroke="#fff" stroke-width="2"><rect x="4" y="11" width="16" height="9" rx="1"/><path d="M4 15h16M12 4v7"/></svg></div>
    <h3>4. Final Presentation</h3>
    <p>The finished desserts are crafted with care and presented beautifully, creating a cohesive and memorable dessert experience that enhances your celebration.</p>
  </div>
</div>

<div class="abs script" style="left:0;top:1800px;width:1200px">Our Gallery</div>
<h2 class="abs heading" style="left:0;top:1852px;width:1200px">Featured creations</h2>
<div class="abs gallery">
  <div class="tile" role="img" aria-label="Frosted cake bites in rows" style="background:radial-gradient(circle at 40% 40%,#efe2cc,#b8946e 50%,#4e2f22)"></div>
  <div class="tile" role="img" aria-label="Dessert bar table with many bites" style="background:radial-gradient(circle at 50% 55%,#e6d3b4,#a9785a 50%,#4a2c20)"></div>
  <div class="tile" role="img" aria-label="Cream-topped bites on a white stand" style="background:radial-gradient(circle at 55% 45%,#f6f1ea,#b9aa98 55%,#3e3530)"></div>
  <div class="tile" role="img" aria-label="Event dessert display" style="background:radial-gradient(circle at 45% 60%,#c9a07a,#6e4630 50%,#1f140f)"></div>
  <div class="tile" role="img" aria-label="Round white chocolate bites" style="background:radial-gradient(circle at 50% 50%,#f7efdc,#d6bf94 50%,#8a6e4a)"></div>
  <div class="tile" role="img" aria-label="Brownie squares with hazelnut" style="background:radial-gradient(circle at 50% 45%,#9a6446,#5a3222 50%,#24130d)"></div>
</div>
<a class="abs btn btn-pink" style="left:494px;top:2630px">View Dessert Bar Catering</a>

<div class="abs seasonal" role="img" aria-label="Tasting box desserts spread across a table" style="background:linear-gradient(90deg,#4a2a1e,#9a6a52 18%,#6b4030 40%,#8a6650 62%,#d9c9b4 82%,#5a3a2a)"></div>
<div class="abs seasonal-panel">
  <div class="script">Intentional Dessert</div>
  <h2 class="heading" style="font-size:40px;margin-top:4px">Seasonal tasting boxes</h2>
  <p style="width:640px;margin:14px auto 0;font-size:14px;line-height:1.5;color:var(--muted)">Our seasonal tasting boxes are thoughtfully curated collections of small dessert bites inspired by the flavors of the season and special occasions. Each box is designed as a tasting experience, highlighting a variety of textures, flavor profiles, and ingredient pairings in just a few intentional bites.</p>
  <a class="btn btn-pink" style="margin-top:16px">View Current Tasting Box</a>
</div>

<div class="abs script" style="left:0;top:3496px;width:1200px">Curated Gatherings</div>
<h2 class="abs heading" style="left:0;top:3544px;width:1200px">Who it's for</h2>
<div class="abs aud-card" role="img" aria-label="Wedding reception table" style="left:120px;width:280px;background:radial-gradient(circle at 50% 30%,#e6b478,#8a5230 50%,#2a1a12)"></div>
<div class="abs aud-card" role="img" aria-label="Corporate evening event" style="left:452px;width:296px;background:radial-gradient(circle at 50% 30%,#c99a70,#4a5a78 45%,#3a1e28)"></div>
<div class="abs aud-card" role="img" aria-label="Wrapped seasonal gift box" style="left:800px;width:288px;background:radial-gradient(circle at 50% 55%,#c2343c,#a85a50 40%,#e6d8c8)"></div>
<div class="abs aud-label" style="left:120px;width:280px"><b>Weddings &amp; Celebrations</b>Elegant dessert bars</div>
<div class="abs aud-label" style="left:452px;width:296px"><b>Corporate &amp; Private Events</b>Refined small bites</div>
<div class="abs aud-label" style="left:800px;width:288px"><b>Seasonal &amp; Giftable</b>Limited-release tasting</div>

<footer class="abs footer"></footer>
<div class="abs" role="img" aria-label="Flowers beside dessert bites" style="left:212px;top:4228px;width:160px;height:384px;background:linear-gradient(180deg,#e2c04e,#8a7a40 45%,#2e2218)"></div>
<div class="abs" role="img" aria-label="Pumpkin and autumn treats" style="left:828px;top:4228px;width:164px;height:384px;background:linear-gradient(180deg,#2e221a,#6a4a30 45%,#d8782c)"></div>
<div class="abs logo-badge" style="left:548px;top:4240px;width:104px;height:104px;font-size:19px">Lumetta</div>
<div class="abs contact">
  (555) 340-7712<br>
  hello@lumettasmallbites.example<br>
  Lumetta Small Bite Catering<br>
  48 Orchard Lane, Suite 2, Riverside Bay, CA 90000
</div>
<div class="abs social" style="left:540px"></div>
<div class="abs social" style="left:584px"></div>
<div class="abs social" style="left:628px"></div>
<div class="abs legal">© Lumetta Small Bite Catering LLC. All rights reserved.</div>

</body>
</html>
```